TOVR Enterprise
company business card and envolpe design
TOVR Enterprise -
Creative Brief
Professional
Neeraj Pillai
Director
114, 2c, 2nd floor, Rukminibai Market, Rukminibai Bldg No. 6, Pepper Orchard Lane, Mumbai - 400017.
pillaineeraj41@postvela.example
Should look same as the logo. Business card and Stationery should also be very professional.
TOVR Enterprise is the parent company underwhich many other firms are going to start. So back of the card should be designed in way that i can add the name of other firms.

```html
<!DOCTYPE html>
<html lang="en">
<head>
<meta charset="utf-8">
<title>TOVR Enterprise – Business Cards</title>
<link href="https://fonts.googleapis.com/css2?family=Open+Sans:wght@400;600;700&display=swap" rel="stylesheet">
<style>
  :root {
    --backdrop: #e9e6e2;
    --card: #ffffff;
    --brand-red: #b3141c;
    --brand-red-dark: #7d0a10;
    --grey: #8a8a8a;
    --grey-light: #d4d4d4;
    --ink: #333333;
    --rule: #c9c9c9;
  }
  * { margin: 0; padding: 0; box-sizing: border-box; }
  html, body { width: 1200px; height: 852px; overflow: hidden; }
  body {
    background: var(--backdrop);
    font-family: "Open Sans", Arial, sans-serif;
    color: var(--ink);
    position: relative;
  }
  .card {
    position: absolute;
    width: 600px;
    height: 340px;
    background: var(--card);
    border-radius: 14px;
    overflow: hidden;
    box-shadow: 0 10px 26px rgba(0,0,0,0.22);
  }
  .card--front { left: 110px; top: 60px; }
  .card--back { left: 490px; top: 450px; }
  .swoosh { position: absolute; left: 0; bottom: 0; width: 600px; height: 110px; }

  .brand { position: absolute; display: flex; align-items: center; gap: 12px; }
  .brand__mark { width: 58px; height: 58px; border-radius: 50%; background: var(--brand-red); flex: none; }
  .brand__name { font-weight: 700; font-size: 36px; color: var(--brand-red); letter-spacing: 1px; line-height: 1; white-space: nowrap; }

  .person__name { font-weight: 700; font-size: 17px; color: var(--brand-red); }
  .person__role { font-size: 12px; color: var(--grey); margin-bottom: 12px; }
  .address { font-size: 12.5px; line-height: 1.5; color: var(--ink); }

  .contacts { position: absolute; list-style: none; font-size: 12.5px; line-height: 1; white-space: nowrap; }
  .contacts li { display: flex; align-items: center; gap: 8px; height: 22px; }
  .contacts svg { width: 13px; height: 13px; fill: var(--brand-red); flex: none; }

  .divider { position: absolute; width: 1px; background: var(--rule); }

  /* front layout */
  .card--front .brand { left: 36px; top: 36px; }
  .card--front .person { position: absolute; left: 96px; top: 120px; width: 240px; text-align: right; }
  .card--front .divider { left: 350px; top: 118px; height: 110px; }
  .card--front .contacts { left: 362px; top: 126px; }

  /* back layout */
  .card--back .person { position: absolute; left: 260px; top: 36px; width: 300px; padding-left: 12px; border-left: 1px solid var(--rule); }
  .card--back .brand { left: 36px; top: 150px; }
  .card--back .contacts { left: 272px; top: 160px; }
</style>
</head>
<body>

<svg width="0" height="0" style="position:absolute" aria-hidden="true">
  <defs>
    <linearGradient id="redSweep" x1="0" y1="0" x2="1" y2="0">
      <stop offset="0" stop-color="#7d0a10"/>
      <stop offset="0.5" stop-color="#d11a22"/>
      <stop offset="1" stop-color="#8e0c12"/>
    </linearGradient>
    <linearGradient id="greySweep" x1="0" y1="0" x2="1" y2="0">
      <stop offset="0" stop-color="#9a9a9a"/>
      <stop offset="0.6" stop-color="#e0e0e0"/>
      <stop offset="1" stop-color="#bdbdbd"/>
    </linearGradient>
    <symbol id="icon-phone" viewBox="0 0 24 24"><path d="M6.6 10.8a15 15 0 0 0 6.6 6.6l2.2-2.2c.3-.3.7-.4 1-.2 1.1.4 2.3.6 3.600.6.6 0 1 .4 1 1V20c0 .6-.4 1-1 1A17 17 0 0 1 3 4c0-.6.4-1 1-1h3.5c.6 0 1 .4 1 1 0 1.3.2 2.5.6 3.6.1.3 0 .7-.2 1z"/></symbol>
    <symbol id="icon-mobile" viewBox="0 0 24 24"><path d="M7 2h10a2 2 0 0 1 2 2v16a2 2 0 0 1-2 2H7a2 2 0 0 1-2-2V4a2 2 0 0 1 2-2zm0 3v12h10V5zm5 13.5a1 1 0 1 0 0 2 1 1 0 0 0 0-2z"/></symbol>
    <symbol id="icon-fax" viewBox="0 0 24 24"><path d="M6 2h10v6H6zM3 9h18v10H3zm3 3v2h3v-2zm0 3v2h3v-2zm5-3v2h3v-2z"/></symbol>
    <symbol id="icon-mail" viewBox="0 0 24 24"><path d="M12 2a10 10 0 1 0 5 18.7l-1-1.7A8 8 0 1 1 20 12v1.5a1.5 1.5 0 0 1-3 0V7h-2v1a5 5 0 1 0 .8 7.3A3.5 3.5 0 0 0 22 13.5V12A10 10 0 0 0 12 2zm0 13a3 3 0 1 1 0-6 3 3 0 0 1 0 6z"/></symbol>
  </defs>
</svg>

<section class="card card--front" aria-label="Business card front">
  <div class="brand">
    <span class="brand__mark"></span>
    <span class="brand__name">TOVR Enterprise</span>
  </div>

  <div class="person">
    <p class="person__name">Neeraj Pillai</p>
    <p class="person__role">Director</p>
    <p class="address">114, 2c, 2nd floor, Rukminibai Market,<br>Rukminibai Bldg No. 6, Pepper Orchard<br>Lane, Mumbai - 400017.</p>
  </div>

  <span class="divider"></span>

  <ul class="contacts">
    <li><svg><use href="#icon-phone"/></svg>+910000471120</li>
    <li><svg><use href="#icon-mobile"/></svg>+910000583904</li>
    <li><svg><use href="#icon-fax"/></svg>+910000471135</li>
    <li><svg><use href="#icon-mail"/></svg>pillaineeraj41@postvela.example</li>
  </ul>

  <svg class="swoosh" viewBox="0 0 600 110" preserveAspectRatio="none" aria-hidden="true">
    <path d="M0 40 C180 95 420 95 600 35 L600 110 L0 110 Z" fill="url(#greySweep)"/>
    <path d="M0 70 C200 108 420 100 600 55 L600 110 L0 110 Z" fill="url(#redSweep)"/>
  </svg>
</section>

<section class="card card--back" aria-label="Business card back">
  <div class="person">
    <p class="person__name">Neeraj Pillai</p>
    <p class="person__role">Director</p>
    <p class="address">114, 2c, 2nd floor, Rukminibai Market,<br>Rukminibai Bldg No. 6, Pepper Orchard Lane,<br>Mumbai - 400017.</p>
  </div>

  <div class="brand">
    <span class="brand__mark"></span>
    <span class="brand__name">TOVR</span>
  </div>

  <ul class="contacts">
    <li><svg><use href="#icon-phone"/></svg>+910000471120</li>
    <li><svg><use href="#icon-mobile"/></svg>+910000583904</li>
    <li><svg><use href="#icon-fax"/></svg>+910000471135</li>
    <li><svg><use href="#icon-mail"/></svg>pillaineeraj41@postvela.example</li>
  </ul>

  <svg class="swoosh" viewBox="0 0 600 110" preserveAspectRatio="none" aria-hidden="true">
    <path d="M0 55 C200 100 430 95 600 30 L600 110 L0 110 Z" fill="url(#greySweep)"/>
    <path d="M0 78 C220 110 440 100 600 50 L600 110 L0 110 Z" fill="url(#redSweep)"/>
  </svg>
</section>

</body>
</html>
```